Energieausweis
Zielgruppe
Zielgruppe sind Immobilieninteressenten - Verwendung in einem Immobilienmagazin und im Internet.
Aufgabenstellung
Ab dem 1. Mai muss in Deutschland die Energie-Effizienzklasse bei Immobilienangeboten mit veröffentlicht werden. Das kann man nüchtern in Zahlen darstellen, aber auch in einer netten Grafik. In der Anlage finden 2 von uns gekaufte Pixbarun-Bilder. Das Bild mit dem Männchen ist eine sehr nette Idee. Da wir in unserem Logo auch ein Männchen haben, bietet es sich an, ein LindenHaus-Männchen zusammen mit der bunten Grafik zu gestalten. (Das Pixbarun-Bild soll nur die Idee erklären - bitte nicht verwenden). Wenn die Grafik fertig ist, legen wir einen Pfeil zur Kennzeichnung der jeweiligen Energieklasse hinzu. Das heisst, wir haben dann für jede Energieklasse eine entsprechende Vorlage und dem richtig platzierten Pfeil. Weiter finden sie in der Anlage unser Firmenlogo zur freuen Verwendung.

```html
<!DOCTYPE html>
<html lang="de">
<head>
<meta charset="utf-8">
<title>Energieausweis – Vorlagen</title>
<link rel="stylesheet" href="https://fonts.googleapis.com/css2?family=Arimo:wght@400;700&display=swap">
<style>
  :root {
    --navy: #004c7c;
    --white: #ffffff;
    --class-a: #0a6e31;
    --class-b: #239c29;
    --class-c: #a3bd08;
    --class-d: #e2d90f;
    --class-e: #edb700;
    --class-f: #e97100;
    --class-g: #e12122;
    --accent-red: #e2001a;
  }
  * { margin: 0; padding: 0; box-sizing: border-box; }
  html, body { width: 848px; height: 1200px; overflow: hidden; }
  body { background: var(--navy); font-family: "Arimo", Arial, sans-serif; position: relative; }

  .label-card {
    position: absolute; width: 378px; height: 532px;
    background: var(--white); border-radius: 10px; overflow: hidden;
  }
  .label-card--tl { left: 30px; top: 31px; }
  .label-card--tr { left: 439px; top: 31px; }
  .label-card--bl { left: 30px; top: 634px; }
  .label-card--br { left: 439px; top: 634px; }

  .label-card--a { --accent: var(--class-a); }
  .label-card--c { --accent: var(--class-c); }
  .label-card--e { --accent: var(--class-e); }
  .label-card--red { --accent: var(--accent-red); }

  .title-bar {
    position: absolute; left: 15px; top: 15px; width: 348px; height: 57px;
    background: var(--navy); border-radius: 6px; color: var(--white);
    text-align: center;
  }
  .title-bar__title {
    display: block; font-weight: 700; font-size: 37px; line-height: 1;
    letter-spacing: 0.2px; padding-top: 6px;
  }
  .title-bar__law {
    position: absolute; right: 9px; bottom: 5px;
    font-size: 9px; font-weight: 400; line-height: 1;
  }
  .consumption-heading {
    position: absolute; right: 26px; top: 81px;
    color: var(--navy); font-size: 14.5px; font-weight: 700; letter-spacing: 0.1px;
  }
  .mascot-area {
    position: absolute; left: 29px; top: 143px; width: 187px; height: 180px;
    border-radius: 8px;
    background: radial-gradient(circle at 70% 35%, var(--accent) 0 12%, transparent 13%),
                linear-gradient(160deg, #1d6596, var(--navy));
  }
  .consumption-value {
    position: absolute; right: 25px; top: 157px; text-align: right;
    color: var(--accent); font-weight: 700; line-height: 1;
  }
  .consumption-value__number { display: block; font-size: 36px; letter-spacing: -0.5px; }
  .consumption-value__unit { display: block; font-size: 35px; margin-top: 3px; }

  .class-scale { position: absolute; left: 0; top: 0; width: 378px; height: 532px; }
  .class-scale text {
    font-family: "Arimo", Arial, sans-serif; font-weight: 700; font-size: 54px;
    fill: var(--white); text-anchor: middle;
  }
  .bar-a { fill: var(--class-a); } .bar-b { fill: var(--class-b); }
  .bar-c { fill: var(--class-c); } .bar-d { fill: var(--class-d); }
  .bar-e { fill: var(--class-e); } .bar-f { fill: var(--class-f); }
  .bar-g { fill: var(--class-g); }
</style>
</head>
<body>

<svg width="0" height="0" style="position:absolute">
  <defs>
    <g id="energy-scale">
      <polygon class="bar-a" points="34,790 75,761 116,790 116,989 34,989"/>
      <polygon class="bar-b" points="130,760 171,731 212,760 212,989 130,989"/>
      <polygon class="bar-c" points="227,730 268,698 309,730 309,989 227,989"/>
      <polygon class="bar-d" points="323,696 364,661 405,696 405,989 323,989"/>
      <polygon class="bar-e" points="420,660 461,620 502,660 502,989 420,989"/>
      <polygon class="bar-f" points="516,616 557,571 598,616 598,989 516,989"/>
      <polygon class="bar-g" points="612,570 653,520 694,570 694,989 612,989"/>
      <text x="75" y="976">A</text>
      <text x="171" y="976">B</text>
      <text x="268" y="978">C</text>
      <text x="364" y="978">D</text>
      <text x="461" y="976">E</text>
      <text x="557" y="980">F</text>
      <text x="653" y="980">G</text>
    </g>
  </defs>
</svg>

<section class="label-card label-card--tl label-card--a">
  <header class="title-bar">
    <span class="title-bar__title">ENERGIEAUSWEIS</span>
    <span class="title-bar__law">gemäß den §§ 16 ff. Energieeinsparverordnung (EnEV)</span>
  </header>
  <p class="consumption-heading">ERFASSTER ENERGIEVERBRAUCH</p>
  <div class="mascot-area" role="img" aria-label="Illustration: laufendes Männchen trägt ein kleines Haus in der Klassenfarbe"></div>
  <p class="consumption-value"><span class="consumption-value__number">XXXXX</span><span class="consumption-value__unit">kWh</span></p>
  <svg class="class-scale" viewBox="0 0 724 1018" aria-label="Energieeffizienzklassen A bis G"><use href="#energy-scale"/></svg>
</section>

<section class="label-card label-card--tr label-card--c">
  <header class="title-bar">
    <span class="title-bar__title">ENERGIEAUSWEIS</span>
    <span class="title-bar__law">gemäß den §§ 16 ff. Energieeinsparverordnung (EnEV)</span>
  </header>
  <p class="consumption-heading">ERFASSTER ENERGIEVERBRAUCH</p>
  <div class="mascot-area" role="img" aria-label="Illustration: laufendes Männchen trägt ein kleines Haus in der Klassenfarbe"></div>
  <p class="consumption-value"><span class="consumption-value__number">XXXXX</span><span class="consumption-value__unit">kWh</span></p>
  <svg class="class-scale" viewBox="0 0 724 1018" aria-label="Energieeffizienzklassen A bis G"><use href="#energy-scale"/></svg>
</section>

<section class="label-card label-card--bl label-card--e">
  <header class="title-bar">
    <span class="title-bar__title">ENERGIEAUSWEIS</span>
    <span class="title-bar__law">gemäß den §§ 16 ff. Energieeinsparverordnung (EnEV)</span>
  </header>
  <p class="consumption-heading">ERFASSTER ENERGIEVERBRAUCH</p>
  <div class="mascot-area" role="img" aria-label="Illustration: laufendes Männchen trägt ein kleines Haus in der Klassenfarbe"></div>
  <p class="consumption-value"><span class="consumption-value__number">XXXXX</span><span class="consumption-value__unit">kWh</span></p>
  <svg class="class-scale" viewBox="0 0 724 1018" aria-label="Energieeffizienzklassen A bis G"><use href="#energy-scale"/></svg>
</section>

<section class="label-card label-card--br label-card--red">
  <header class="title-bar">
    <span class="title-bar__title">ENERGIEAUSWEIS</span>
    <span class="title-bar__law">gemäß den §§ 16 ff. Energieeinsparverordnung (EnEV)</span>
  </header>
  <p class="consumption-heading">ERFASSTER ENERGIEVERBRAUCH</p>
  <div class="mascot-area" role="img" aria-label="Illustration: laufendes Männchen trägt ein kleines Haus in der Klassenfarbe"></div>
  <p class="consumption-value"><span class="consumption-value__number">XXXXX</span><span class="consumption-value__unit">kWh</span></p>
  <svg class="class-scale" viewBox="0 0 724 1018" aria-label="Energieeffizienzklassen A bis G"><use href="#energy-scale"/></svg>
</section>

</body>
</html>
```